Mirvald Health & Wellness needs a fresh and interesting website

I need a rebrand and redevelopment of my website, www.tessapinlowe.com
Our mission is provide bespoke , lifestyle medicine , everyone has their own path to health. and we are creating a personalized experience for people to life their life to the fullest
Mirvald - means sea lands
I need an landing page and about page and potentially a few project launch pages , I have been using Wordpress for my basic information and then I use Kartra for the launch pages of my programs since I can edit those easily.

Target Market(s)

Corporate and individual's who are interested in a different perspective on health and wellness , and living with a chronic illness

Industry/Entity Type

Health, lifestyle , wellness coaching and medicine

Coding

Number of Pages Required

2 page

Font styles to use
Other font styles liked:
• look into the logo

Requirements
Must have
• the logo I uploaded
Nice to have
• I want a fresh perspective on health, I have bamboo, hibiscus vibes in my logo , but also like more of a water vibe/ I want something earthy but not too boho it needs to be clean
Should not have
• every other holistic health vibe,

```html
<!DOCTYPE html>
<html lang="en">
<head>
<meta charset="utf-8">
<title>Mirvald Health &amp; Wellness</title>
<link href="https://fonts.googleapis.com/css2?family=Playfair+Display:wght@400;500&family=Outfit:wght@300;400;500;600&display=swap" rel="stylesheet">
<style>
:root{
  --teal:#1b88a6;
  --teal-deep:#137892;
  --green:#6cbd1f;
  --ink:#1f2528;
  --body:#3c4246;
  --mist:#eef1f6;
  --line:#cfdbe3;
  --white:#ffffff;
}
*{box-sizing:border-box;margin:0;padding:0}
html,body{width:1200px;height:5333px;overflow:hidden}
body{position:relative;background:var(--white);font-family:'Outfit',sans-serif;color:var(--body)}
.abs{position:absolute}
.serif{font-family:'Playfair Display',serif;font-weight:400}
.accent{color:var(--teal)}
.btn{position:absolute;display:flex;align-items:center;justify-content:center;background:var(--teal);color:var(--white);font-size:13px;font-weight:600;letter-spacing:.3px;border-radius:22px;box-shadow:3px 3px 0 var(--green);text-transform:uppercase;height:42px}
.photo{position:absolute}

/* header + hero */
.hero{position:absolute;left:0;top:0;width:1200px;height:625px;background:linear-gradient(180deg,#d7dcdf 0%,#bcc3c6 40%,#8c7a55 75%,#6e5a3c 100%)}
.socials{position:absolute;left:100px;top:16px;display:flex;gap:10px}
.socials span,.foot-social span{width:33px;height:33px;border-radius:50%;background:var(--teal);display:block}
.phone{position:absolute;right:100px;top:16px;display:flex;align-items:center;gap:10px;font-size:15px;color:var(--ink)}
.phone i{width:33px;height:33px;border-radius:50%;background:var(--teal);display:flex;align-items:center;justify-content:center}
.nav{position:absolute;top:82px;font-size:15px;color:var(--ink);display:flex;gap:48px;letter-spacing:.3px}
.brand{position:absolute;left:520px;top:30px;width:160px;text-align:center;color:var(--teal)}
.brand .dot{width:30px;height:30px;border-radius:50%;border:2px solid var(--teal);margin:0 auto 4px}
.brand b{font-family:'Playfair Display',serif;font-weight:400;font-size:30px;display:block;line-height:1}
.hero h1{position:absolute;left:0;width:1200px;top:396px;text-align:center;color:var(--white);font-size:36px;line-height:46px}

/* about */
.about-frame{left:114px;top:700px;width:452px;height:502px;border:2px solid var(--teal)}
.about h2{left:650px;top:720px;font-size:38px;line-height:46px;color:var(--ink)}
.about p{position:absolute;left:651px;width:450px;font-size:12.5px;line-height:26px;text-align:justify}

/* offerings */
.band{position:absolute;left:0;width:1200px;background:var(--mist)}
.sec-title{position:absolute;left:0;width:1200px;text-align:center;font-size:38px;color:var(--ink)}
.card{position:absolute;width:478px;height:492px;background:var(--white);border:1px solid #a8d2df}
.card .img{height:271px}
.card h3{font-family:'Playfair Display',serif;font-weight:400;font-size:22px;color:var(--ink);text-align:center;margin-top:22px}
.card p{font-size:12.5px;line-height:26px;text-align:center;width:420px;margin:12px auto 0}

/* banner */
.banner{position:absolute;left:0;top:2012px;width:1200px;height:373px;background:linear-gradient(180deg,#4c5248 0%,#6d6f55 55%,#8c8a4c 100%)}
.banner h2{position:absolute;left:0;width:1200px;top:106px;text-align:center;color:var(--white);font-size:36px;line-height:46px}

/* services */
.svc-box{position:absolute;width:453px;background:var(--mist);padding:54px 28px 0}
.svc-box h3{font-family:'Playfair Display',serif;font-weight:400;font-size:23px;color:var(--ink)}
.svc-box p{font-size:12.5px;line-height:26px;margin-top:16px;text-align:justify}
.svc-box .btn{position:absolute;left:28px;width:186px}

/* spotlights */
.quote{position:absolute;width:273px;height:302px;background:var(--white);box-shadow:0 2px 8px rgba(0,0,0,.08);padding:54px 26px 0}
.quote p{font-size:13px;line-height:24px;font-style:italic;text-align:center}
.quote .who{text-align:center;color:var(--teal);font-weight:600;font-size:18px;margin-top:18px}
.quote .mark{position:absolute;right:-10px;top:-12px;width:46px;height:46px;border-radius:50%;background:var(--green);color:var(--white);font-family:'Playfair Display',serif;font-size:44px;line-height:56px;text-align:center}
.arrow{position:absolute;top:4098px}

/* contact */
.contact h2{left:650px;top:4424px;font-size:38px;line-height:46px;color:var(--teal)}
.field{position:absolute;height:38px;border:1px solid var(--line);border-radius:4px;background:var(--white);font-size:12px;color:var(--ink);padding:10px 16px}

/* footer */
.footer{position:absolute;left:0;top:4979px;width:1200px;height:354px;background:var(--teal-deep);color:var(--white)}
.footer h4{font-weight:500;font-size:18px;margin-bottom:12px}
.footer li{list-style:none;font-size:13px;line-height:30px}
.foot-col{position:absolute;top:70px}
.foot-brand{position:absolute;left:100px;top:74px;width:240px;text-align:center}
.foot-brand .dot{width:56px;height:56px;border-radius:50%;border:2px solid var(--white);margin:0 auto 8px}
.foot-brand b{font-family:'Playfair Display',serif;font-weight:400;font-size:50px;line-height:1;display:block}
.foot-social{display:flex;gap:14px;margin-top:14px}
.foot-social span{background:var(--white)}
.rule{position:absolute;left:100px;width:1000px;top:291px;height:1px;background:rgba(255,255,255,.45)}
.copy{position:absolute;left:0;width:1200px;top:310px;text-align:center;font-size:14px}
</style>
</head>
<body>

<header class="hero" role="img" aria-label="Woman standing with arms raised on a mountain peak above misty lakes">
  <div class="socials"><span></span><span></span><span></span><span></span></div>
  <div class="phone"><i><svg width="16" height="16" viewBox="0 0 24 24"><path fill="#fff" d="M6.6 10.8a15 15 0 0 0 6.6 6.6l2.2-2.2a1 1 0 0 1 1-.25 11.4 11.4 0 0 0 3.6.57 1 1 0 0 1 1 1V20a1 1 0 0 1-1 1A17 17 0 0 1 3 4a1 1 0 0 1 1-1h3.5a1 1 0 0 1 1 1c0 1.25.2 2.45.57 3.57a1 1 0 0 1-.25 1z"/></svg></i>+1 888 888 8888</div>
  <nav class="nav" style="left:100px"><span>HOME</span><span>ABOUT</span><span>FALL MINI RETREAT</span></nav>
  <div class="brand"><div class="dot"></div><b>Mirvald</b></div>
  <nav class="nav" style="left:736px"><span>SERVICES</span><span>TESTIMONIALS</span><span>CONTACT</span></nav>
  <h1 class="serif">Tessa Pinlowe<br>Build Your Courage</h1>
  <span class="btn" style="left:516px;top:510px;width:165px">Get Started »</span>
</header>

<section class="about">
  <div class="abs about-frame"></div>
  <div class="photo" role="img" aria-label="Portrait of the practitioner in a red hat and scarf seated on stone steps" style="left:100px;top:712px;width:452px;height:502px;background:linear-gradient(160deg,#7d8f62,#a36a5a 50%,#4d6a8e)"></div>
  <h2 class="abs serif"><span class="accent">Hi, I’m</span> Dr Tessa P Pinlowe<br>DACM, L.Ac.</h2>
  <p style="top:828px">At a young age, I discovered the transformative power of Eastern Medicine when it helped me overcome lung concerns, propelling me toward my dreams as a young athlete. Years later, I faced a pivotal choice: How could I best serve and heal my community? The answer was crystal clear—Eastern Medicine.</p>
  <p style="top:966px">As an Eastern Medicine doctor, I’ve had the privilege of positively impacting my community through integrative health choices. My journey began after seven years of nurturing creativity and leadership in theatre costume design, when I made the life-altering decision to merge my love for art and science in the field of Acupuncture and Traditional East Asian Medicine (TEAM).</p>
  <span class="btn" style="left:652px;top:1144px;width:188px">Get To Know Me »</span>
</section>

<section class="band" style="top:1298px;height:714px">
  <h2 class="sec-title serif" style="top:64px"><span class="accent">New</span> Offerings</h2>
  <div class="card" style="left:100px;top:145px">
    <div class="img" role="img" aria-label="Couple embracing beneath autumn trees" style="background:linear-gradient(135deg,#c98a2a,#8a6b3c 55%,#6f7a56)"></div>
    <h3>Fall into yourself Mini Retreat</h3>
    <p>Join us for a delightful retreat experience right in the heart of the city, as we come together to honor this season of harvest and letting go, a time to turn inward to expand.</p>
    <span class="btn" style="left:144px;top:425px;width:186px">Register Now »</span>
  </div>
  <div class="card" style="left:615px;top:145px">
    <div class="img" role="img" aria-label="Woman walking through a green wheat field" style="background:linear-gradient(180deg,#3d5e4a,#6f8f5a 60%,#87a26a)"></div>
    <h3>Fall into yourself Mini Retreat</h3>
    <p>Join us for a delightful retreat experience right in the heart of the city, as we come together to honor this season of harvest and letting go, a time to turn inward to expand.</p>
    <span class="btn" style="left:144px;top:425px;width:186px">Register Now »</span>
  </div>
</section>

<section class="banner" role="img" aria-label="Sunlit forest clearing with tall pines">
  <h2 class="serif">Your Companion To Sorting Through<br>Life's Challenges</h2>
  <span class="btn" style="left:505px;top:220px;width:188px">Register Now »</span>
</section>

<section class="services">
  <h2 class="sec-title serif" style="top:2444px"><span class="accent">My</span> Services</h2>

  <div class="photo" role="img" aria-label="Woman lying down receiving facial acupuncture" style="left:590px;top:2527px;width:453px;height:363px;background:linear-gradient(180deg,#caa08a,#8a5f4a)"></div>
  <div class="svc-box" style="left:157px;top:2561px;height:287px">
    <h3>Acupuncture &amp; Eastern Medicine</h3>
    <p>Sed ut perspiciatis unde omnis iste natus error sit voluptatem accusantium doloremque laudantium, totam rem aperiam, eaque ipsa quae ab illo inventore veritatis</p>
    <span class="btn" style="top:190px">Discover More »</span>
  </div>

  <div class="photo" role="img" aria-label="Practitioner giving a relaxing shoulder treatment to a man" style="left:161px;top:2954px;width:454px;height:360px;background:linear-gradient(150deg,#c9b9a6,#7f8ca0 60%,#3d6ea8)"></div>
  <div class="svc-box" style="left:586px;top:2987px;height:290px">
    <h3>Resilience specialist</h3>
    <p>Sed ut perspiciatis unde omnis iste natus error sit voluptatem accusantium doloremque laudantium, totam rem aperiam, eaque ipsa quae ab illo inventore veritatis</p>
    <span class="btn" style="top:190px">Discover More »</span>
  </div>

  <div class="photo" role="img" aria-label="Expectant mother seated on an exercise ball in a bright room" style="left:590px;top:3380px;width:453px;height:360px;background:linear-gradient(160deg,#f1ece6,#d9c5b5 60%,#d98a98)"></div>
  <div class="svc-box" style="left:157px;top:3413px;height:284px">
    <h3>Fertility specialist</h3>
    <p>Sed ut perspiciatis unde omnis iste natus error sit voluptatem accusantium doloremque laudantium, totam rem aperiam, eaque ipsa quae ab illo inventore veritatis</p>
    <span class="btn" style="top:188px">Discover More »</span>
  </div>
</section>

<section class="band" style="top:3834px;height:524px">
  <h2 class="sec-title serif" style="top:64px"><span class="accent">Client</span> Spotlights</h2>
</section>
<svg class="arrow" style="left:66px" width="20" height="36" viewBox="0 0 20 36"><path d="M18 2 2 18l16 16" fill="none" stroke="#3c4246" stroke-width="2"/></svg>
<svg class="arrow" style="left:1120px" width="20" height="36" viewBox="0 0 20 36"><path d="M2 2l16 16L2 34" fill="none" stroke="#3c4246" stroke-width="2"/></svg>
<div class="quote" style="left:106px;top:3983px"><span class="mark">”</span><p>Sed ut perspiciatis unde omnis iste natus error sit voluptatem accusantium doloremque laudantium, totam rem aperiam, eaque ipsa quae ab illo inventore veritatis quasi architecto beatae vitae dicta sunt explicabo. Nemo enim ipsam voluptatem quia voluptas sit aspernatur</p><div class="who">John smith</div></div>
<div class="quote" style="left:447px;top:3983px"><span class="mark">”</span><p>Sed ut perspiciatis unde omnis iste natus error sit voluptatem accusantium doloremque laudantium, totam rem aperiam, eaque ipsa quae ab illo inventore veritatis quasi architecto beatae vitae dicta sunt explicabo. Nemo enim ipsam voluptatem quia voluptas sit aspernatur</p><div class="who">John smith</div></div>
<div class="quote" style="left:789px;top:3983px"><span class="mark">”</span><p>Sed ut perspiciatis unde omnis iste natus error sit voluptatem accusantium doloremque laudantium, totam rem aperiam, eaque ipsa quae ab illo inventore veritatis quasi architecto beatae vitae dicta sunt explicabo. Nemo enim ipsam voluptatem quia voluptas sit aspernatur</p><div class="who">John smith</div></div>

<section class="contact">
  <div class="photo" role="img" aria-label="Smiling practitioner seated with a notebook in a bright studio" style="left:0;top:4358px;width:600px;height:621px;background:linear-gradient(160deg,#f3efe9,#e3c9b3 50%,#d8743e)"></div>
  <h2 class="abs serif">Do You Want To Inquire<br><span style="color:var(--ink)">About A Service?</span></h2>
  <div class="abs" style="left:648px;top:4530px;font-size:16px;font-weight:500;color:var(--ink)">Feel free to reach out.</div>
  <div class="abs" style="left:648px;top:4563px;font-size:13px">Send me a message here if you would like to connect!</div>
  <div class="field" style="left:646px;top:4612px;width:217px">Full Name</div>
  <div class="field" style="left:882px;top:4612px;width:217px">Phone Number</div>
  <div class="field" style="left:646px;top:4672px;width:217px">Email Address</div>
  <div class="field" style="left:882px;top:4672px;width:217px">Subject</div>
  <div class="field" style="left:646px;top:4728px;width:453px;height:112px">Your Message</div>
  <span class="btn" style="left:772px;top:4867px;width:198px">Connect With Me »</span>
</section>

<footer class="footer">
  <div class="foot-brand"><div class="dot"></div><b>Mirvald</b><div style="font-size:13px;letter-spacing:5px;margin-top:6px">HEALTH &amp; WELLNESS</div></div>
  <div class="foot-col" style="left:439px"><h4>Quick Links</h4><ul><li>Home</li><li>About</li><li>Fall Mini Retreat</li><li>Services</li><li>Testimonials</li><li>Contact</li></ul></div>
  <div class="foot-col" style="left:656px"><h4>Other Links</h4><ul><li>Contact Sales</li><li>Legal Hub</li><li>Privacy Policy</li><li>Trust &amp; Security</li><li>Cookie Preferences</li></ul></div>
  <div class="foot-col" style="left:896px"><h4>Contact Info</h4><ul><li>+1 888 - 888 - 8888</li><li>hello@tessapinlowe.com</li></ul><div class="foot-social"><span></span><span></span><span></span><span></span></div></div>
  <div class="rule"></div>
  <div class="copy">©Copyright 2024 Mirvald Health &amp; Wellness. All Rights Reserved.</div>
</footer>

</body>
</html>
```